Business Card - high end, modern health care

Hey designers!

We need a double sided business card for the boutique, cutting edge physical therapy rehabilitation centre in Sydney's Northern Beaches.

With the most qualified physios in the area The Ridgeline Motion Clinic does what other physiotherapy practices do not, we take our time with our patients giving them longer appointments, better physios and therefor faster results!

We guarantee that the service people receive at TRMC will be unparalleled.

Hence we need a business card to reflect our modern, boutique, high end service. The final design needs to reflect that we are in a class of our own yet with the feel of beachside retreat.

Below I have attached our logo in both blue on white and white on blue. The exact colour is;
and the font that we have used in our logo is Tex Gyre Aventador.

I like the idea of the blue as the main colour as it is more eye catching and our signage onto the main road will be in this blue and in the interest of consistency across marketing the blue needs to be a part of the design. However I would appreciate a few designs onto a wooden background as this is a visual theme within the fitout of the practice.

The design needs to be of standard size (91x55mm).

Target Market(s)

We target people who have an end outcome in mind and those who have had poor experiences with other providers and ensure that everyone gets the care that they deserve with a premium service that is tailored to the individuals circumstances. As a premium service, the target market is highly educated, business and tech savvy with the additional target market of elderly people who have self funded their retirement and see value in paying for the best ongoing rehabilitation to maintain independence.

Industry/Entity Type

Physical Therapy

Contact Information for Business Card

Name, designation( Titled Musculoskeletal Physiotherapist... there will also be those in the company that have multiple designations ie 5 or 6 words long), phone number, email, facebook, instagram, address

Font styles to use
Sans Serif

Colors

Designer to choose colors to be used in the design.

Requirements
Must have
• Front - The logo as large as possible, blue or wooden theme, and all of the important details.
• Back - A blank space/lines on which to write appointment times (no "Appointment, date, time" etc.)
Nice to have
• facebook url
• logos for facebook and instagram
• Mini logos for the phone and email?

```html
<!DOCTYPE html>
<html lang="en">
<head>
<meta charset="utf-8">
<title>The Ridgeline Motion Clinic – Business Card</title>
<link href="https://fonts.googleapis.com/css2?family=Montserrat:wght@600&family=Oswald:wght@600&family=Roboto:wght@400&display=swap" rel="stylesheet">
<style>
  :root {
    --brand-blue: #0b5bbd;
    --brand-blue-deep: #0a4fa6;
    --wash-blue: #dbe6f3;
    --ink-grey: #333a44;
    --paper: #ffffff;
    --backdrop: #2a2d31;
  }
  * { margin: 0; padding: 0; box-sizing: border-box; }
  html, body { width: 1200px; height: 900px; overflow: hidden; }
  body {
    background: var(--backdrop);
    display: flex;
    flex-direction: column;
    align-items: center;
    justify-content: center;
    gap: 50px;
  }
  .card {
    position: relative;
    width: 600px;
    height: 363px;
    border-radius: 26px;
    overflow: hidden;
    box-shadow: 0 14px 30px rgba(0,0,0,.35);
  }

  /* Contact side */
  .card--contact { background: var(--paper); }
  .contact__ring {
    position: absolute;
    left: 300px; top: 80px;
    width: 330px; height: 330px;
    border-radius: 50%;
    border: 46px solid var(--wash-blue);
  }
  .contact__band { position: absolute; left: 0; bottom: 0; width: 600px; height: 70px; }
  .contact__socials {
    position: absolute; right: 34px; bottom: 14px;
    display: flex; gap: 12px;
  }
  .social-dot {
    width: 18px; height: 18px; border-radius: 50%;
    background: var(--paper);
  }
  .person { position: absolute; left: 44px; top: 34px; }
  .person__name {
    font-family: "Oswald", sans-serif;
    font-weight: 600;
    font-size: 42px;
    line-height: 1;
    color: var(--brand-blue);
    letter-spacing: .5px;
    text-transform: uppercase;
  }
  .person__credentials {
    margin-top: 8px;
    font-family: "Roboto", sans-serif;
    font-size: 12px;
    line-height: 1.35;
    color: var(--ink-grey);
  }
  .contact-list {
    position: absolute; left: 44px; top: 148px;
    list-style: none;
    display: flex; flex-direction: column; gap: 14px;
  }
  .contact-item { display: flex; align-items: center; gap: 14px; }
  .contact-item__icon {
    width: 38px; height: 38px; border-radius: 50%;
    border: 1.6px solid var(--brand-blue);
    display: flex; align-items: center; justify-content: center;
    flex-shrink: 0;
  }
  .contact-item__icon svg { width: 20px; height: 20px; }
  .contact-item__text {
    font-family: "Roboto", sans-serif;
    font-size: 14px;
    line-height: 1.3;
    color: var(--ink-grey);
  }

  /* Brand side */
  .card--brand { background: var(--brand-blue); }
  .brand__halo {
    position: absolute; left: 70px; top: 20px;
    width: 320px; height: 320px; border-radius: 50%;
    background: rgba(255,255,255,.07);
  }
  .brand__lockup {
    position: absolute; left: 70px; top: 0; height: 100%;
    display: flex; align-items: center; gap: 20px;
  }
  .brand__dot {
    width: 74px; height: 74px; border-radius: 50%;
    background: var(--paper);
    flex-shrink: 0;
  }
  .brand__name {
    font-family: "Montserrat", sans-serif;
    font-weight: 600;
    color: var(--paper);
    text-transform: uppercase;
    line-height: 1.15;
  }
  .brand__name-main { display: block; font-size: 38px; letter-spacing: 1px; }
  .brand__name-sub { display: block; font-size: 22px; letter-spacing: 8px; }
</style>
</head>
<body>

  <section class="card card--contact" aria-label="Contact side">
    <div class="contact__ring" aria-hidden="true"></div>
    <svg class="contact__band" viewBox="0 0 600 70" aria-hidden="true">
      <path d="M310 70 C330 70 338 36 372 30 L600 30 L600 70 Z" fill="var(--brand-blue)"/>
    </svg>
    <div class="contact__socials" aria-label="Social media">
      <span class="social-dot"></span>
      <span class="social-dot"></span>
    </div>

    <div class="person">
      <h1 class="person__name">Daniel Hart</h1>
      <p class="person__credentials">M.Phty(Musc.)<br>B.App.Sc(Physio), APAM</p>
    </div>

    <ul class="contact-list">
      <li class="contact-item">
        <span class="contact-item__icon">
          <svg viewBox="0 0 24 24" fill="none" stroke="var(--brand-blue)" stroke-width="1.6" stroke-linecap="round" stroke-linejoin="round"><path d="M5 3h4l2 5-2.5 1.5a11 11 0 0 0 6 6L16 13l5 2v4a2 2 0 0 1-2 2A17 17 0 0 1 3 5a2 2 0 0 1 2-2z"/><path d="M15 3a6 6 0 0 1 6 6M15 7a2 2 0 0 1 2 2"/></svg>
        </span>
        <span class="contact-item__text">00 9876 543 210<br>00 9876 543 210</span>
      </li>
      <li class="contact-item">
        <span class="contact-item__icon">
          <svg viewBox="0 0 24 24" fill="none" stroke="var(--brand-blue)" stroke-width="1.6" stroke-linecap="round"><rect x="6" y="3" width="12" height="18" rx="6"/><path d="M12 7v4"/></svg>
        </span>
        <span class="contact-item__text">hello@ridgelinemotion.com<br>www.ridgelinemotion.com</span>
      </li>
      <li class="contact-item">
        <span class="contact-item__icon">
          <svg viewBox="0 0 24 24" fill="none" stroke="var(--brand-blue)" stroke-width="1.6" stroke-linejoin="round"><path d="M12 21s-7-6.5-7-12a7 7 0 0 1 14 0c0 5.5-7 12-7 12z"/><circle cx="12" cy="9" r="2.6"/></svg>
        </span>
        <span class="contact-item__text">18 Pittwater Road, Suite 4<br>Manly, NSW 2095</span>
      </li>
    </ul>
  </section>

  <section class="card card--brand" aria-label="Brand side">
    <div class="brand__halo" aria-hidden="true"></div>
    <div class="brand__lockup">
      <span class="brand__dot" aria-hidden="true"></span>
      <h2 class="brand__name">
        <span class="brand__name-main">The Ridgeline</span>
        <span class="brand__name-sub">Motion Clinic</span>
      </h2>
    </div>
  </section>

</body>
</html>
```